Free Offer Book Cover

I am creating a funnel page where I offer a free download of a PDF called. Twelve-Week Launch Kit. A road map for new leaders. I have included samples of other book covers. It can look like a book, or a checklist, or something that illustrates what they are getting. Bright Harbor Coaching is the company if you could get the logo into the book cover as well.

Target Market(s)

New leaders, young professionals

Font styles to use
Sans Serif

Requirements
Must have
• Name of content. Twelve-Week Launch Kit for new leaders.

```html
<!DOCTYPE html>
<html lang="en">
<head>
<meta charset="utf-8">
<title>Twelve-Week Launch Kit – Bright Harbor Coaching</title>
<link rel="stylesheet" href="https://fonts.googleapis.com/css2?family=Arimo:wght@400;700&display=swap">
<style>
  :root {
    --stage-top: #10263d;
    --stage-bottom: #353f47;
    --cover-charcoal: #2e2e2f;
    --cover-slate-top: #24374b;
    --cover-slate-bottom: #30404a;
    --slate-edge: #8a96a3;
    --frame: #0d1e3d;
    --band-light: #b9c5d8;
    --band-dark: #1b2841;
    --ink-dark: #1b2a44;
    --ink-light: #f2f2f2;
    --corner-deep: #040a16;
    --corner-mid: #0b1a33;
  }
  * { margin: 0; padding: 0; box-sizing: border-box; }
  html, body {
    width: 1200px;
    height: 1200px;
    overflow: hidden;
    background: linear-gradient(160deg, var(--stage-top), var(--stage-bottom));
    font-family: "Arimo", Arial, sans-serif;
  }
  .stage {
    width: 1200px;
    height: 1200px;
    display: flex;
    align-items: center;
    justify-content: center;
    gap: 40px;
  }
  .cover {
    width: 540px;
    height: 691px;
    display: block;
  }
  .cover-bg--charcoal { fill: var(--cover-charcoal); }
  .cover-edge { fill: none; stroke: var(--slate-edge); stroke-width: 2; }
  .cover-frame { fill: none; stroke: var(--frame); stroke-width: 6; }
  .title-band { fill: var(--band-light); }
  .title-text { fill: var(--ink-dark); font-weight: 700; font-size: 35px; }
  .subtitle-band { fill: var(--band-dark); }
  .subtitle-text { fill: var(--ink-light); font-weight: 700; font-size: 28px; }
  .subtitle-rule { stroke: var(--ink-light); stroke-width: 2; }
  .field-label { fill: var(--ink-light); font-weight: 700; font-size: 34px; }
  .field-line { stroke: var(--ink-light); stroke-width: 1.6; stroke-dasharray: 5 2 1 2; }
  .brand-name { fill: var(--ink-light); font-weight: 700; font-size: 26px; letter-spacing: 3px; }
</style>
</head>
<body>
<main class="stage">

  <svg class="cover cover--charcoal" viewBox="0 0 700 896" xmlns="http://www.w3.org/2000/svg" aria-label="Twelve-Week Launch Kit for new leaders, charcoal cover">
    <defs>
      <clipPath id="charcoal-clip"><rect width="700" height="896"/></clipPath>
      <radialGradient id="charcoal-corner" cx="0.75" cy="0.75" r="0.8">
        <stop offset="0" stop-color="var(--corner-deep)"/>
        <stop offset="1" stop-color="var(--corner-mid)"/>
      </radialGradient>
    </defs>
    <rect class="cover-bg--charcoal" width="700" height="896"/>
    <circle cx="662" cy="858" r="206" fill="url(#charcoal-corner)" clip-path="url(#charcoal-clip)"/>
    <path class="cover-frame" d="M55 36 H644 A22 22 0 0 0 666 58 V835 A22 22 0 0 0 644 857 H55 A22 22 0 0 0 36 835 V58 A22 22 0 0 0 55 36 Z"/>
    <rect class="title-band" x="41" y="146" width="520" height="53"/>
    <text class="title-text" x="540" y="186" text-anchor="end">TWELVE-WEEK LAUNCH KIT</text>
    <polygon class="subtitle-band" points="186,207 546,207 546,243 168,243"/>
    <line class="subtitle-rule" x1="218" y1="226" x2="288" y2="226"/>
    <text class="subtitle-text" x="541" y="236" text-anchor="end">for new leaders.</text>
    <text class="field-label" x="118" y="378">WHO</text>
    <line class="field-line" x1="241" y1="381" x2="579" y2="381"/>
    <text class="field-label" x="118" y="455">WHAT</text>
    <line class="field-line" x1="241" y1="456" x2="579" y2="456"/>
    <text class="field-label" x="116" y="525">HOW</text>
    <line class="field-line" x1="241" y1="527" x2="579" y2="527"/>
    <text class="field-label" x="118" y="602">WHEN</text>
    <line class="field-line" x1="241" y1="604" x2="579" y2="604"/>
    <text class="brand-name" x="515" y="778" text-anchor="middle">BRIGHT HARBOR</text>
    <text class="brand-name" x="515" y="814" text-anchor="middle">COACHING</text>
  </svg>

  <svg class="cover cover--slate" viewBox="0 0 700 896" xmlns="http://www.w3.org/2000/svg" aria-label="Twelve-Week Launch Kit for new leaders, slate cover">
    <defs>
      <clipPath id="slate-clip"><rect width="700" height="896"/></clipPath>
      <linearGradient id="slate-fill" x1="0" y1="0" x2="1" y2="1">
        <stop offset="0" stop-color="var(--cover-slate-top)"/>
        <stop offset="1" stop-color="var(--cover-slate-bottom)"/>
      </linearGradient>
      <radialGradient id="slate-corner" cx="0.75" cy="0.75" r="0.8">
        <stop offset="0" stop-color="var(--corner-deep)"/>
        <stop offset="1" stop-color="var(--corner-mid)"/>
      </radialGradient>
    </defs>
    <rect width="700" height="896" fill="url(#slate-fill)"/>
    <circle cx="662" cy="858" r="206" fill="url(#slate-corner)" clip-path="url(#slate-clip)"/>
    <rect class="cover-edge" x="1" y="1" width="698" height="894"/>
    <path class="cover-frame" d="M55 36 H644 A22 22 0 0 0 666 58 V835 A22 22 0 0 0 644 857 H55 A22 22 0 0 0 36 835 V58 A22 22 0 0 0 55 36 Z"/>
    <rect class="title-band" x="41" y="146" width="520" height="53"/>
    <text class="title-text" x="540" y="186" text-anchor="end">TWELVE-WEEK LAUNCH KIT</text>
    <polygon class="subtitle-band" points="186,207 546,207 546,243 168,243"/>
    <line class="subtitle-rule" x1="218" y1="226" x2="288" y2="226"/>
    <text class="subtitle-text" x="541" y="236" text-anchor="end">for new leaders.</text>
    <text class="field-label" x="118" y="378">WHO</text>
    <line class="field-line" x1="241" y1="381" x2="579" y2="381"/>
    <text class="field-label" x="118" y="455">WHAT</text>
    <line class="field-line" x1="241" y1="456" x2="579" y2="456"/>
    <text class="field-label" x="116" y="525">HOW</text>
    <line class="field-line" x1="241" y1="527" x2="579" y2="527"/>
    <text class="field-label" x="118" y="602">WHEN</text>
    <line class="field-line" x1="241" y1="604" x2="579" y2="604"/>
    <text class="brand-name" x="515" y="778" text-anchor="middle">BRIGHT HARBOR</text>
    <text class="brand-name" x="515" y="814" text-anchor="middle">COACHING</text>
  </svg>

</main>
</body>
</html>
```